Marist Valley College Brenthurst Letterhead

Our college is called Marist Valley College Brenthurst. We would like to request a few letterhead design options to choose from please. We look forward to seeing some new and fresh ideas for our College Letterhead.

Please note that the College has the following PMS Colours:
MAROON – PMS 229C
BLUE – PMS 2747C
GOLD – PMS 871C
YELLOW – PMS 123C

Our College Motto is:
Faith seeking Understanding.
I have attached a copy of our current letterhead and College Logo.

Please note that the letterhead must include the following details:

Marist Valley College Brenthurst
Faith Seeking Understanding
Phone: 8472 5518
Fax:8415 7730
Address: 214 Kellaway Street Brenthurst 3041
Mail:PO BOX 4857 Marlow Heights VIC 3045 Australia
ABN 61 507 284 913

www.mvcbrenthurst-example.net
https://twitter.com/mvcbrenthurst
https://www.pinterest.com/mvcbrenthurst
https://www.facebook.com/MVCBrenthurst
vidhub-example.com (search MVC Brenthurst)

Please feel free to contact me on the below detail if I can further assist.

Regards,
Joanna Whitcombe
reception@mvcbrenthurst-example.net
PH: 8472 5518

Target Market(s)

College Community

Industry/Entity Type

Education

Font styles to use
Other font styles liked:
• You decide

Requirements
Must have
• See Project Description
Nice to have
• see Project Description

```html
<!DOCTYPE html>
<html lang="en">
<head>
<meta charset="utf-8">
<title>Marist Valley College Brenthurst – Stationery</title>
<link href="https://fonts.googleapis.com/css2?family=Source+Sans+3:ital,wght@0,400;0,600;0,700;1,400&display=swap" rel="stylesheet">
<style>
  :root {
    --backdrop: #e9e6e2;
    --paper: #ffffff;
    --paper-shade: #f4f4f4;
    --maroon: #8c2c5f;
    --flap: #9b4575;
    --navy: #23305e;
    --gold: #e8c21a;
    --ink: #3e3e3e;
    --ink-soft: #5a5a5a;
    --rule: #9a9a9a;
  }
  * { box-sizing: border-box; margin: 0; padding: 0; }
  html, body { width: 1200px; height: 840px; overflow: hidden; }
  body {
    background: var(--backdrop);
    font-family: "Source Sans 3", "Myriad Pro", Arial, sans-serif;
    color: var(--ink);
    position: relative;
  }
  .sheet {
    position: absolute;
    background: linear-gradient(90deg, var(--paper-shade), var(--paper) 40%);
    box-shadow: 0 2px 8px rgba(0,0,0,.18);
    overflow: hidden;
  }

  /* ---------- Shared pieces ---------- */
  .crest {
    position: absolute; display: flex; align-items: center; gap: 6px;
    font-weight: 600; color: var(--maroon);
  }
  .crest-dot { flex: none; border-radius: 50%; background: var(--navy); }
  .contact { position: absolute; font-size: 8px; line-height: 11.6px; color: var(--ink-soft); white-space: nowrap; }
  .contact .org { color: var(--maroon); font-weight: 600; font-size: 8.4px; }
  .contact .row { display: flex; align-items: center; gap: 5px; }
  .icon { width: 7px; height: 7px; flex: none; }
  .social-dot { width: 6px; height: 6px; border-radius: 50%; background: var(--maroon); flex: none; }
  .rule { height: 1px; background: var(--rule); }

  /* ---------- Letterhead ---------- */
  .letterhead { left: 42px; top: 58px; width: 512px; height: 725px; }
  .letterhead .crest { left: 40px; top: 30px; width: 120px; font-size: 9px; line-height: 11px; }
  .letterhead .crest-dot { width: 44px; height: 44px; }
  .letterhead .contact-main { left: 180px; top: 30px; }
  .letterhead .contact-web { left: 322px; top: 30px; padding-left: 9px; border-left: 1px solid var(--maroon); height: 60px; font-size: 7.8px; }

  .letter { position: absolute; left: 64px; top: 178px; width: 384px; font-size: 7.9px; line-height: 12px; color: var(--ink-soft); }
  .letter .salutation { font-weight: 700; color: var(--ink); margin-bottom: 17px; }
  .letter p { text-align: justify; hyphens: auto; margin-bottom: 24px; }
  .letter .closing { margin-bottom: 8px; }
  .signature { width: 98px; height: 30px; background: linear-gradient(90deg, #e6e6e6, #f6f6f6); }

  .motto-line { position: absolute; display: flex; align-items: center; gap: 4px; font-style: italic; font-size: 8px; color: var(--ink-soft); }
  .letterhead .motto-line { left: 23px; top: 698px; }
  .letterhead .motto-line .rule { width: 358px; }

  /* ---------- Envelope front ---------- */
  .envelope-front { left: 595px; top: 58px; width: 558px; height: 277px; }
  .envelope-front .crest { left: 30px; top: 42px; width: 110px; font-size: 9px; line-height: 11px; }
  .envelope-front .crest-dot { width: 54px; height: 54px; }
  .envelope-front .contact { left: 143px; top: 36px; padding-left: 11px; border-left: 1px solid var(--maroon); }
  .return { position: absolute; left: 0; right: 28px; top: 238px; text-align: right; font-size: 8px; line-height: 11.6px; color: var(--ink-soft); }
  .return .motto-row { display: flex; align-items: center; gap: 6px; font-style: italic; }
  .return .motto-row .rule { flex: 1; }

  /* ---------- Envelope back ---------- */
  .envelope-back { left: 595px; top: 355px; width: 558px; height: 277px; background: var(--paper); }
  .envelope-back svg { position: absolute; inset: 0; }
  .envelope-back .crest { left: 0; right: 0; top: 30px; justify-content: center; font-size: 9px; color: var(--paper); }
  .envelope-back .crest-dot { width: 20px; height: 20px; }
  .envelope-back .site { position: absolute; left: 0; right: 0; top: 244px; text-align: center; font-size: 8.4px; letter-spacing: 1px; color: var(--ink-soft); }
</style>
</head>
<body>

<!-- Letterhead -->
<section class="sheet letterhead">
  <div class="crest"><span class="crest-dot"></span><span>Marist Valley College Brenthurst</span></div>

  <div class="contact contact-main">
    <div class="org">Marist Valley College Brenthurst</div>
    <div>214 Kellaway Street Brenthurst 3041</div>
    <div>ABN: 61 507 284 913</div>
    <div class="row"><svg class="icon" viewBox="0 0 10 10"><path d="M2 1 L4 1 L4.6 3 L3.4 4 Q4.4 6 6 6.6 L7 5.4 L9 6 L9 8 Q9 9 8 9 Q1 8.5 1 2 Q1 1 2 1Z" fill="var(--maroon)"/></svg>8472 5518</div>
    <div class="row"><svg class="icon" viewBox="0 0 10 10"><rect x="2.5" y="1" width="5" height="3" fill="var(--maroon)"/><rect x="1" y="4" width="8" height="5" rx="1" fill="var(--maroon)"/></svg>8415 7730</div>
  </div>

  <div class="contact contact-web">
    <div class="row"><span class="social-dot"></span>www.mvcbrenthurst-example.net</div>
    <div class="row"><span class="social-dot"></span>chirpnet-example.com/mvcbrenthurst</div>
    <div class="row"><span class="social-dot"></span>www.pinboard-example.com/mvcbrenthurst</div>
    <div class="row"><span class="social-dot"></span>www.friendpage-example.com/MVCBrenthurst</div>
    <div class="row"><span class="social-dot"></span>vidhub-example.com (search MVC Brenthurst)</div>
  </div>

  <div class="letter" lang="en">
    <div class="salutation">Dear Sam Whitford,</div>
    <p>Lorem Ipsum is simply dummy text of the printing and typesetting industry. Lorem Ipsum has been the industry's standard dummy text ever since the 1500s, when an unknown printer took a galley of type and scrambled it to make a type specimen book. It has survived not only five centuries, but also the leap into electronic typesetting, remaining essentially unchanged. It was popularised in the 1960s with the release of Transfertype sheets containing Lorem Ipsum passages, and more recently with desktop publishing software like Quarto Layout including versions of Lorem Ipsum.</p>
    <p>It is a long established fact that a reader will be distracted by the readable content of a page when looking at its layout. The point of using Lorem Ipsum is that it has a more-or-less normal distribution of letters, as opposed to using 'Content here, content here', making it look like readable English. Many desktop publishing packages and web page editors now use Lorem Ipsum as their default model text, and a search for 'lorem ipsum' will uncover many web sites still in their infancy. Various versions have evolved over the years, sometimes by accident, sometimes on purpose (injected humour and the like).</p>
    <p>The standard chunk of Lorem Ipsum used since the 1500s is reproduced below for those interested. Sections 1.10.32 and 1.10.33 from "de Finibus Bonorum et Malorum" by Verano are also reproduced in their exact original form, accompanied by English versions from the 1914 translation by H. Pellman. There are many variations of passages of Lorem Ipsum available, but the majority have suffered alteration in some form, by injected humour, or randomised words which don't look even slightly believable.</p>
    <p>It is a long established fact that a reader will be distracted by the readable content of a page when looking at its layout. The point of using Lorem Ipsum is that it has a more-or-less normal distribution of letters, as opposed to using 'Content here, content here', making it look like readable English. Many desktop publishing packages and web page editors now use Lorem Ipsum as their default model text, and a search for 'lorem ipsum' will uncover many web sites still in their infancy. Various versions have evolved over the years, sometimes by accident, sometimes on purpose (injected humour and the like).</p>
    <div class="closing">Sincerely Yours,</div>
    <div class="signature" role="img" aria-label="Handwritten signature"></div>
  </div>

  <div class="motto-line"><span>Faith Seeking Understanding</span><span class="rule"></span></div>
</section>

<!-- Envelope front -->
<section class="sheet envelope-front">
  <div class="crest"><span class="crest-dot"></span><span>Marist Valley College Brenthurst</span></div>
  <div class="contact">
    <div class="org">Marist Valley College Brenthurst</div>
    <div>214 Kellaway Street Brenthurst 3041</div>
    <div>ABN: 61 507 284 913</div>
    <div class="row"><svg class="icon" viewBox="0 0 10 10"><path d="M2 1 L4 1 L4.6 3 L3.4 4 Q4.4 6 6 6.6 L7 5.4 L9 6 L9 8 Q9 9 8 9 Q1 8.5 1 2 Q1 1 2 1Z" fill="var(--maroon)"/></svg>8472 5518</div>
    <div class="row"><svg class="icon" viewBox="0 0 10 10"><rect x="2.5" y="1" width="5" height="3" fill="var(--maroon)"/><rect x="1" y="4" width="8" height="5" rx="1" fill="var(--maroon)"/></svg>8415 7730</div>
    <div class="row"><svg class="icon" viewBox="0 0 10 10"><circle cx="5" cy="5" r="4" fill="none" stroke="var(--maroon)"/><path d="M1 5 H9 M5 1 Q2 5 5 9 Q8 5 5 1" fill="none" stroke="var(--maroon)" stroke-width=".7"/></svg>www.mvcbrenthurst-example.net</div>
  </div>
  <div class="return">
    <div>PO BOX 4857 Marlow Heights VIC 3045 Australia</div>
    <div class="motto-row"><span class="rule"></span><span>Faith Seeking Understanding</span></div>
  </div>
</section>

<!-- Envelope back -->
<section class="sheet envelope-back">
  <svg viewBox="0 0 558 277" width="558" height="277" aria-hidden="true">
    <path d="M14 60 Q10 62 10 70 L8 268 L4 277" fill="none" stroke="#b5b5b5" stroke-width="1"/>
    <path d="M544 60 Q548 62 548 70 L550 268 L554 277" fill="none" stroke="#b5b5b5" stroke-width="1"/>
    <path d="M0 0 H558 L552 12 Q542 52 498 60 L279 88 L60 60 Q16 52 6 12 Z" fill="var(--flap)"/>
  </svg>
  <div class="crest"><span class="crest-dot"></span><span>Marist Valley College Brenthurst</span></div>
  <div class="site">www.mvcbrenthurst-example.net</div>
</section>

</body>
</html>
```